Billboard design for retail kitchen cabinet business

We have a large 7,000 square-foot showroom of beautiful kitchen cabinet displays of all different designs and price ranges. In business for over 50 years with expert designers.
Full size Halvard Media 14' X 48' billboard
Target Market(s)
Retail public on high traffic Los Angeles streets

```html
<!DOCTYPE html>
<html lang="en">
<head>
<meta charset="utf-8">
<title>Hearthline Cabinetry – Billboard</title>
<link rel="stylesheet" href="https://fonts.googleapis.com/css2?family=Oswald:wght@700&family=Roboto+Condensed:wght@700&display=swap">
<style>
  :root {
    --page-bg: #e4e4e4;
    --brand-yellow: #f6b31a;
    --brand-charcoal: #4a4a4a;
    --ink-dark: #3a3a3a;
    --paper: #ffffff;
    --tile-grey: #eeeeee;
    --room-white: #f4f3f0;
    --room-grey: #cfcdc8;
    --room-steel: #a9aaae;
    --island-navy: #3c3a55;
  }
  html, body {
    margin: 0;
    padding: 0;
    width: 984px;
    height: 1200px;
    overflow: hidden;
    background: var(--page-bg);
  }
  .canvas {
    width: 984px;
    height: 1200px;
    display: flex;
    align-items: center;
    justify-content: center;
  }
  .billboard {
    width: 920px;
    height: 249px;
    display: block;
    box-shadow: 0 14px 22px rgba(0,0,0,0.22);
  }
  .headline { font-family: "Oswald", sans-serif; font-weight: 700; fill: var(--paper); }
  .subline { font-family: "Roboto Condensed", sans-serif; font-weight: 700; fill: var(--ink-dark); }
  .phone-number { font-family: "Roboto Condensed", sans-serif; font-weight: 700; fill: var(--ink-dark); }
  .web-address { font-family: "Roboto Condensed", sans-serif; font-weight: 700; fill: var(--paper); }
  .web-address .accent { fill: var(--brand-yellow); }
  .tagline { font-family: "Roboto Condensed", sans-serif; font-weight: 700; fill: var(--paper); }
  .brand-name { font-family: "Roboto Condensed", sans-serif; font-weight: 700; fill: var(--ink-dark); }
</style>
</head>
<body>
<main class="canvas">
  <svg class="billboard" viewBox="0 0 1480 400" xmlns="http://www.w3.org/2000/svg">
    <defs>
      <linearGradient id="roomLight" x1="0" y1="0" x2="1" y2="0">
        <stop offset="0" stop-color="var(--paper)"/>
        <stop offset="0.25" stop-color="var(--room-white)"/>
        <stop offset="0.6" stop-color="var(--room-grey)"/>
        <stop offset="1" stop-color="var(--room-white)"/>
      </linearGradient>
      <radialGradient id="islandShade" cx="0.58" cy="0.85" r="0.35">
        <stop offset="0" stop-color="var(--island-navy)" stop-opacity="0.75"/>
        <stop offset="1" stop-color="var(--island-navy)" stop-opacity="0"/>
      </radialGradient>
      <radialGradient id="steelShade" cx="0.3" cy="0.45" r="0.3">
        <stop offset="0" stop-color="var(--room-steel)" stop-opacity="0.6"/>
        <stop offset="1" stop-color="var(--room-steel)" stop-opacity="0"/>
      </radialGradient>
    </defs>

    <rect class="board-base" x="0" y="0" width="1480" height="400" fill="var(--paper)"/>
    <polygon class="tile-wash" points="380,0 820,0 820,125 560,125" fill="var(--tile-grey)" opacity="0.6"/>

    <g class="showroom-photo" role="img" aria-label="Photo of a bright white showroom kitchen with pendant lights, stainless appliances and a navy island">
      <polygon points="760,0 1480,0 1480,347 820,347 760,290" fill="url(#roomLight)"/>
      <polygon points="760,0 1480,0 1480,347 820,347 760,290" fill="url(#steelShade)"/>
      <polygon points="760,0 1480,0 1480,347 820,347 760,290" fill="url(#islandShade)"/>
    </g>

    <g class="phone-icon" fill="none" stroke="var(--brand-yellow)" stroke-linecap="round">
      <path d="M44 44 q-4 20 12 36 q16 16 34 12" stroke-width="11"/>
      <path d="M66 40 a12 12 0 0 1 12 12" stroke-width="5"/>
      <path d="M68 28 a24 24 0 0 1 24 24" stroke-width="5"/>
    </g>
    <text class="phone-number" x="115" y="88" font-size="78" textLength="420" lengthAdjust="spacingAndGlyphs">(310) 555-0148</text>

    <polygon class="headline-band" points="0,125 665,125 745,215 665,307 0,307" fill="var(--brand-yellow)"/>
    <text class="headline" x="35" y="210" font-size="82" textLength="600" lengthAdjust="spacingAndGlyphs">CREATE YOUR DREAM</text>
    <text class="headline" x="35" y="290" font-size="82" textLength="240" lengthAdjust="spacingAndGlyphs">KITCHEN</text>
    <text class="subline" x="305" y="258" font-size="32">WITH HEARTHLINE</text>
    <text class="subline" x="305" y="290" font-size="32">CABINETRY</text>

    <polygon class="brand-panel" points="755,110 878,233 755,356 632,233" fill="var(--paper)"/>
    <text class="brand-name" x="755" y="228" font-size="34" text-anchor="middle">HEARTHLINE</text>
    <text class="brand-name" x="755" y="264" font-size="34" text-anchor="middle">CABINETRY</text>

    <polygon class="web-band" points="0,307 797,307 762,394 0,394" fill="var(--brand-charcoal)"/>
    <circle class="globe-icon" cx="62" cy="350" r="24" fill="var(--brand-yellow)"/>
    <g fill="none" stroke="var(--paper)" stroke-width="2.5">
      <circle cx="62" cy="350" r="14"/>
      <ellipse cx="62" cy="350" rx="6" ry="14"/>
      <line x1="48" y1="350" x2="76" y2="350"/>
    </g>
    <text class="web-address" x="117" y="366" font-size="46">www.<tspan class="accent">hearthlinekitchens</tspan>.net</text>

    <polygon class="tagline-band" points="820,347 1480,347 1480,394 784,394" fill="var(--brand-yellow)"/>
    <text class="tagline" x="1150" y="384" font-size="38" text-anchor="middle" textLength="570" lengthAdjust="spacingAndGlyphs">BEAUTIFYING KITCHEN SINCE 1965</text>

    <rect class="base-rule" x="0" y="394" width="1480" height="6" fill="var(--brand-yellow)"/>
  </svg>
</main>
</body>
</html>
```